Flyer-Design für Lindenhof
Zielgruppe
Lindenhof Berlin. Spielmöglichkeit an über 50 Flippergeräten. Verleih von Flipper- und Arcadegeräten. Verkauf, Reparatur, Restaurierung von Flipperautomaten. Firmenevents, Geburtstage, Feiern in der Lindenhof.
Aufgabenstellung
Faltblatt Din-lang 6-seitig

```html
<!DOCTYPE html>
<html lang="de">
<head>
<meta charset="utf-8">
<title>Lindenhof Berlin – Faltblatt DIN lang</title>
<link href="https://fonts.googleapis.com/css2?family=Quicksand:wght@400;500;600;700&display=swap" rel="stylesheet">
<style>
:root{
  --blue:#3d5cb4;
  --blue-deep:#2f4a99;
  --slate:#4b4f58;
  --slate-dark:#343944;
  --paper:#ffffff;
  --mist:#e8e9ec;
  --ink:#4e525a;
  --stage:#eeeff1;
}
*{box-sizing:border-box;margin:0;padding:0}
html,body{width:889px;height:1200px;overflow:hidden;background:var(--stage);font-family:"Quicksand",sans-serif;color:var(--ink)}
.spread{position:absolute;left:34px;width:820px;height:580px;display:flex;background:var(--paper);box-shadow:0 6px 18px rgba(0,0,0,.18)}
.spread--outside{top:13px}
.spread--inside{top:607px}
.panel{position:relative;width:33.3333%;height:100%;overflow:hidden}
.photo{position:absolute;left:0;right:0}
.block{position:absolute;left:0;right:0}
.block--blue{background:var(--blue)}
.block--mist{background:var(--mist)}

/* outside: about */
.about__title{position:absolute;top:26px;left:0;right:0;text-align:center;font-weight:700;color:var(--blue-deep);font-size:15px;letter-spacing:.5px}
.about__rule{position:absolute;top:48px;left:0;width:165px;height:2px;background:var(--blue)}
.about__text{position:absolute;top:66px;left:26px;right:22px;font-size:10.4px;line-height:1.42;text-align:center}
.about__text p{margin-bottom:9px}

/* outside: contact */
.contact{position:absolute;top:232px;left:0;right:0;color:#fff;text-align:center;font-size:9px;line-height:1.35}
.contact__icon{width:22px;height:22px;border-radius:50%;background:#fff;margin:0 auto 6px;display:flex;align-items:center;justify-content:center}
.contact__line{height:1px;background:rgba(255,255,255,.55);margin:10px 30px}
.contact strong{font-weight:700}
.contact__phone,.contact__mail{font-weight:700;font-size:10px}

/* outside: cover */
.cover__name{position:absolute;top:26px;right:22px;color:#fff;font-weight:700;font-size:17px;line-height:1.1;text-align:right;letter-spacing:1px;display:flex;align-items:center;gap:8px}
.cover__name i{display:block;width:12px;height:12px;border-radius:50%;background:#fff}
.visit-badge{position:absolute;top:140px;right:26px;width:72px;height:72px;border-radius:50%;background:var(--slate-dark);border:2px solid #fff;box-shadow:0 0 0 3px var(--slate-dark);color:#fff;font-size:8.5px;font-weight:700;text-align:center;display:flex;align-items:center;justify-content:center;line-height:1.25}
.url-tab{position:absolute;top:256px;left:0;background:var(--blue);color:#fff;font-size:9px;font-weight:700;padding:5px 12px}
.cover__title{position:absolute;top:418px;left:0;right:0;text-align:center;color:#fff}
.cover__title h1{font-size:27px;font-weight:700;letter-spacing:1px;line-height:1.05}
.cover__title .dash{display:flex;align-items:center;justify-content:center;gap:10px;font-size:27px;font-weight:700;letter-spacing:1px}
.cover__title .dash::before,.cover__title .dash::after{content:"";width:44px;height:2px;background:#fff}
.cover__title p{margin-top:10px;font-size:11.5px;font-weight:700;letter-spacing:.5px}

/* inside: trial play */
.trial{position:absolute;top:168px;left:20px;right:20px;text-align:center}
.trial h2{color:var(--blue-deep);font-size:15px;font-weight:700;margin-bottom:8px}
.trial h3{color:var(--blue-deep);font-size:11px;font-weight:700;line-height:1.3;margin-bottom:8px}
.trial p{font-size:10px;line-height:1.35}
.trial .welcome{font-weight:700;color:#333;margin-top:4px}
.hours{position:absolute;top:320px;left:22px;right:22px;font-size:10.5px;font-weight:700;color:var(--blue-deep)}
.hours .head{text-align:center;margin-bottom:6px}
.hours .row{display:flex;justify-content:space-between;margin-bottom:5px}
.prices{position:absolute;top:430px;left:22px;right:22px;color:#fff;font-size:11px}
.prices .row{display:flex;align-items:center;gap:8px;margin-bottom:18px}
.prices .row span:nth-child(2){flex:1;height:1px;background:rgba(255,255,255,.6)}
.prices b{font-weight:700}

/* inside: rental */
.rental{position:absolute;top:244px;left:20px;right:20px;text-align:center;color:#fff}
.rental h2{font-size:15px;font-weight:700;margin-bottom:10px}
.rental h3{font-size:11px;font-weight:700;line-height:1.3;margin-bottom:8px}
.rental p{font-size:10px;line-height:1.35;margin-bottom:6px}
.rental .offer{font-weight:700;margin-top:6px}
.phone-box{display:flex;align-items:center;justify-content:center;gap:10px;margin:8px auto 0;width:180px;border:1.5px solid #fff;border-radius:16px;padding:4px 10px;font-weight:700;font-size:11.5px}
.phone-box i{width:20px;height:20px;border-radius:50%;border:1.5px solid #fff;display:flex;align-items:center;justify-content:center;font-style:normal}
.price-badge{position:absolute;top:160px;right:6px;width:78px;height:70px}
.price-badge__text{position:absolute;inset:0;display:flex;flex-direction:column;align-items:center;justify-content:center;color:#fff;font-size:7.5px;font-weight:700;line-height:1.1;text-align:center}
.price-badge__text b{display:block;background:#fff;color:var(--slate-dark);font-size:11px;padding:1px 5px;margin:2px 0 1px;border-radius:2px}
.price-badge__text small{font-size:5.5px;font-weight:500}

/* checklist */
.checks{position:absolute;top:260px;left:18px;right:16px;list-style:none;font-size:10px;line-height:1.3}
.checks li{display:flex;gap:7px;margin-bottom:15px}
.checks svg{flex:none;margin-top:1px}

/* service tiles */
.tiles{position:absolute;top:470px;left:0;right:0;bottom:0;display:flex;gap:3px;background:#fff}
.tile{flex:1;background:var(--slate);color:#fff;display:flex;flex-direction:column;align-items:center;justify-content:center;gap:10px;font-size:10.5px;font-weight:700;letter-spacing:.3px}
.tile--dark{background:var(--slate-dark)}
</style>
</head>
<body>

<!-- Außenseite -->
<section class="spread spread--outside">
  <div class="panel panel--about">
    <h2 class="about__title">ÜBER UNS</h2>
    <div class="about__rule"></div>
    <div class="about__text">
      <p>In unserer Halle sind ständig rund 60 Flippergeräte aus den Jahren 1977–2018 aufgebaut.</p>
      <p>Bei uns findet man neben dem Kartenkönig aus dem Jahr 1977, der noch über ein Glockenspiel verfügt, über den Hafenbummler mit einem Soundmodul der 1. Generation, dem Stahlwächter 2, der erste Flipper mit einem großen Display, bis zu den neuesten Flippern der Firma Nordlicht – Raumfahrer, Hüter der Sterne, Eisenkrone und auch Starkstrom sowie viele weitere Geräte aus den Jahren der großen Flipperzeiten.</p>
      <p>Auf rund 200 m2 Aufstellfläche gibt es für jeden das passende Thema. Sei es Die Gruselvilla, Geisterjäger, Raumpatrouille oder freie Themen wie Sport, Mittelalter, Zirkus und vieles andere mehr.</p>
    </div>
    <div class="photo" style="top:380px;bottom:0;background:linear-gradient(135deg,#6d6a6e,#a89a8c 45%,#3e4a6a)" role="img" aria-label="Foto: Halle mit Reihen von Flipperautomaten"></div>
  </div>

  <div class="panel panel--contact">
    <div class="photo" style="top:0;height:215px;background:linear-gradient(120deg,#5a3c2c,#8a6a4e 40%,#6f7480 75%,#b3b4b8)" role="img" aria-label="Foto: Mitarbeiter an Flipperautomaten in der Halle"></div>
    <div class="block block--blue" style="top:215px;height:330px"></div>
    <div class="contact">
      <div class="contact__icon"><svg width="12" height="12" viewBox="0 0 12 12"><circle cx="6" cy="4" r="2.4" fill="#3d5cb4"/><path d="M1.5 11.5c0-2.6 2-4.2 4.5-4.2s4.5 1.6 4.5 4.2z" fill="#3d5cb4"/></svg></div>
      <strong>K &amp; R Hallenservice GmbH</strong><br>
      Bereich – Lindenhof –<br>
      Am Ufersteig 4<br>
      12055 Berlin
      <div class="contact__line"></div>
      <div class="contact__icon"><svg width="12" height="12" viewBox="0 0 24 24"><path d="M6.6 10.8a15 15 0 0 0 6.6 6.6l2.2-2.2c.3-.3.7-.4 1-.2 1.1.4 2.3.6 3.6.6.6 0 1 .4 1 1V20c0 .6-.4 1-1 1A17 17 0 0 1 3 4c0-.6.4-1 1-1h3.5c.6 0 1 .4 1 1 0 1.3.2 2.5.6 3.6.1.3 0 .7-.2 1z" fill="#3d5cb4"/></svg></div>
      <div class="contact__phone">+4930 -4412 36 -18</div>
      <div class="contact__line"></div>
      <div class="contact__icon"><svg width="12" height="12" viewBox="0 0 12 12"><rect x="1" y="2.5" width="10" height="7" fill="#3d5cb4"/><path d="M1 2.5l5 4 5-4" stroke="#fff" fill="none"/></svg></div>
      <div class="contact__mail">trohwald@lindenhof-post.de</div>
    </div>
    <div class="photo" style="top:448px;height:108px;left:24px;right:24px;border:5px solid #fff;background:linear-gradient(180deg,#b9cde6 0%,#d6dde6 40%,#8d9099 75%,#a58d86)" role="img" aria-label="Foto: Außenansicht des Hallengebäudes"></div>
  </div>

  <div class="panel panel--cover">
    <div class="photo" style="top:0;height:250px;background:linear-gradient(125deg,#6a6f7a,#9a9aa0 35%,#4a4d58 70%,#2d3340)" role="img" aria-label="Foto: Betreiber steht zwischen Flipperautomaten"></div>
    <div class="photo" style="top:250px;height:150px;background:linear-gradient(120deg,#3a2a22,#8a5a34 40%,#c9a06a 60%,#3b3f4d)" role="img" aria-label="Foto: Flipperautomaten mit Punkteanzeige"></div>
    <div class="cover__name"><i></i><span>LINDENHOF<br>BERLIN</span></div>
    <div class="visit-badge">KOMMT<br>BEI UNS<br>VORBEI!</div>
    <div class="url-tab">WWW.LINDENHOF-BERLIN.DE</div>
    <div class="block block--blue" style="top:400px;height:145px"></div>
    <div class="cover__title">
      <h1>LINDENHOF</h1>
      <div class="dash">BERLIN</div>
      <p>ÜBER 60 AUTOMATEN AUF 200M²</p>
    </div>
  </div>
</section>

<!-- Innenseite -->
<section class="spread spread--inside">
  <div class="panel panel--trial">
    <div class="photo" style="top:0;height:150px;background:linear-gradient(130deg,#2c2a33,#6a5a48 45%,#3a4a7a 80%,#1e2230)" role="img" aria-label="Foto: Spielfeld eines Flipperautomaten"></div>
    <div class="block block--mist" style="top:150px;height:250px"></div>
    <div class="trial">
      <h2>PROBESPIELEN</h2>
      <h3>IHR SEID HERZLICH EINGELADEN<br>ZUM PROBESPIELEN.</h3>
      <p>vereinbart gerne telefonisch einen persönlichen Besichtigungs oder Spieltermin.</p>
      <p class="welcome">Wir freuen uns auf euren Besuch!</p>
    </div>
    <div class="hours">
      <div class="head">ZEITEN:</div>
      <div class="row"><span>FREITAGS</span><span>14:00 - 22:00 UHR</span></div>
      <div class="row"><span>SAMSTAGS</span><span>14:00 - 22:00 UHR</span></div>
    </div>
    <div class="block block--blue" style="top:400px;bottom:0"></div>
    <div class="prices">
      <div class="row"><span>PRO <b>PERSON</b></span><span></span><b>10,00€</b></div>
      <div class="row"><span>FVB <b>MITGLIEDER</b></span><span></span><b>5,00€</b></div>
      <div class="row"><span><b>KINDER</b> UNTER 12</span><span></span><b>FREI</b></div>
    </div>
  </div>

  <div class="panel panel--rental">
    <div class="photo" style="top:0;height:225px;background:linear-gradient(120deg,#5a4a3a,#a8784a 35%,#6a5040 60%,#2b2d36)" role="img" aria-label="Foto: Flipperautomat mit Anzeige Runden Minuten Stunden"></div>
    <div class="block block--blue" style="top:225px;height:245px"></div>
    <svg class="price-badge" viewBox="0 0 78 70" aria-hidden="true"><polygon points="39,2 76,20 76,50 39,68 2,50 2,20" fill="#343944" stroke="#fff" stroke-width="2"/></svg>
    <div class="price-badge" style="pointer-events:none"><div class="price-badge__text">VER-<br>MIETUNG<b>ab 120€</b><small>zzgl. MwSt.</small></div></div>
    <div class="rental">
      <h2>VERMIETUNG</h2>
      <h3>SIE MÖCHTEN IHREN GÄSTEN<br>ETWAS BESONDERES BIETEN?</h3>
      <p>Warum nicht einen oder sogar mehrere Flipper für Ihre Veranstaltung mieten?</p>
      <p>Sie möchten gerne Ihre Party in unserer Halle feiern? Auch das ist möglich.</p>
      <p class="offer">Ihr individuelles Angebot unter:</p>
      <div class="phone-box"><i><svg width="10" height="10" viewBox="0 0 24 24"><path d="M6.6 10.8a15 15 0 0 0 6.6 6.6l2.2-2.2c.3-.3.7-.4 1-.2 1.1.4 2.3.6 3.6.6.6 0 1 .4 1 1V20c0 .6-.4 1-1 1A17 17 0 0 1 3 4c0-.6.4-1 1-1h3.5c.6 0 1 .4 1 1 0 1.3.2 2.5.6 3.6.1.3 0 .7-.2 1z" fill="#fff"/></svg></i>+4930 -4412 36 -18</div>
    </div>
    <div class="tiles">
      <div class="tile">
        <svg width="44" height="44" viewBox="0 0 44 44" fill="none" stroke="#fff" stroke-width="2" stroke-linejoin="round"><path d="M14 6a7 7 0 0 0 6 10l10 10a3 3 0 0 0 4-4L24 12A7 7 0 0 0 14 6l4 4-2 4-4 1-3-4"/><rect x="6" y="30" width="10" height="10"/><path d="M16 32h8l8-3v10H16"/></svg>
        REPARATUR
      </div>
      <div class="tile">
        <svg width="44" height="44" viewBox="0 0 44 44" fill="none" stroke="#fff" stroke-width="2" stroke-linejoin="round"><path d="M10 38L14 6h22l-4 32z"/><circle cx="30" cy="13" r="3"/><path d="M16 30l8-4"/><path d="M22 20l6-5"/></svg>
        SANIERUNG
      </div>
    </div>
  </div>

  <div class="panel panel--services">
    <div class="photo" style="top:0;height:235px;left:0;width:132px;background:linear-gradient(130deg,#6a6e78,#9a8a78 40%,#3a3e4c)" role="img" aria-label="Foto: Mitarbeiter prüft einen Flipper"></div>
    <div class="photo" style="top:0;height:235px;left:138px;background:linear-gradient(130deg,#8a7a6a,#c2a27a 35%,#4a5a7a 70%,#2e3444)" role="img" aria-label="Foto: Flipperreihe in der Halle"></div>
    <div class="block block--mist" style="top:235px;height:235px"></div>
    <ul class="checks">
      <li><svg width="12" height="12" viewBox="0 0 12 12"><circle cx="6" cy="6" r="5" fill="none" stroke="#3d5cb4" stroke-width="1.5"/><path d="M3.5 6l2 2 3-4" stroke="#3d5cb4" stroke-width="1.5" fill="none"/></svg><span>Sie sagen uns welche Geräte Sie wann und wo brauchen, wir kümmern uns darum.</span></li>
      <li><svg width="12" height="12" viewBox="0 0 12 12"><circle cx="6" cy="6" r="5" fill="none" stroke="#3d5cb4" stroke-width="1.5"/><path d="M3.5 6l2 2 3-4" stroke="#3d5cb4" stroke-width="1.5" fill="none"/></svg><span>Sie suchen aus, wir liefern die Geräte an und holen Sie nach dem Event wieder ab.</span></li>
      <li><svg width="12" height="12" viewBox="0 0 12 12"><circle cx="6" cy="6" r="5" fill="none" stroke="#3d5cb4" stroke-width="1.5"/><path d="M3.5 6l2 2 3-4" stroke="#3d5cb4" stroke-width="1.5" fill="none"/></svg><span>Selbstverständlich inklusive Auf- und Abbau und einer Einweisung.</span></li>
      <li><svg width="12" height="12" viewBox="0 0 12 12"><circle cx="6" cy="6" r="5" fill="none" stroke="#3d5cb4" stroke-width="1.5"/><path d="M3.5 6l2 2 3-4" stroke="#3d5cb4" stroke-width="1.5" fill="none"/></svg><span>Sie möchten gerne Ihre Party in unserer Halle feiern? Auch das ist möglich.</span></li>
    </ul>
    <div class="tiles">
      <div class="tile">
        <svg width="44" height="44" viewBox="0 0 44 44" fill="none" stroke="#fff" stroke-width="2" stroke-linejoin="round"><path d="M6 38V22h26v16M6 30h26"/><path d="M32 22V8h6v30"/><circle cx="20" cy="12" r="6"/><path d="M20 9v3l2 2"/></svg>
        VERMIETUNG
      </div>
      <div class="tile tile--dark">
        <svg width="44" height="44" viewBox="0 0 44 44" fill="none" stroke="#fff" stroke-width="2" stroke-linejoin="round"><circle cx="28" cy="12" r="8"/><path d="M31 8.5a4 4 0 1 0 0 7M23 11h6M23 13.5h6"/><path d="M4 28h8l6 2h8a2 2 0 0 1 0 4h-8M26 32l10-5a2 2 0 0 1 3 3L26 38H12l-8-2"/></svg>
        VERKAUF
      </div>
    </div>
  </div>
</section>

</body>
</html>
```